Mezzanine Floor Manufacturer looking for a new business card design

We manufacture mezzanine floors and are providers of racking systems. We provide a range of items/services - simple rack repairs , full warehouse fit outs , manufacturer and install mezzanine floors , partitioning and large turnkey projects. Recently had a new website - www.corvane-shelving.co.uk and would like our business cards updating aswell . Our current card is single sided in the old logo colours (pdf attached) and needs updating.

Target Market(s)

We deal with large projects/ multi national companies and also smaller projects and companies throughout the UK ranging from a single warehouse to a large multi site company.

Industry/Entity Type

Business

Contact Information for Business Card

Will have job title,tel no's, email ,website address etc like example pdf

Requirements
Must have
• Hi - needs to use the colours of the logo & new website. Card needs to be professional

```html
<!DOCTYPE html>
<html lang="en">
<head>
<meta charset="utf-8">
<title>Corvane business card</title>
<link href="https://fonts.googleapis.com/css2?family=Roboto:wght@400;500;700;900&display=swap" rel="stylesheet">
<style>
  :root {
    --brand-red: #c3161f;
    --card-white: #ffffff;
    --swoosh-grey: #8a8a8c;
    --text-grey: #7a7a7a;
    --backdrop: #e4e2de;
  }
  * { margin: 0; padding: 0; box-sizing: border-box; }
  html, body {
    width: 1200px; height: 950px; overflow: hidden;
    background: var(--backdrop);
    font-family: "Roboto", Arial, sans-serif;
  }
  .card {
    position: absolute; left: 240px;
    width: 720px; height: 410px;
    overflow: hidden;
    box-shadow: 0 6px 18px rgba(0,0,0,0.18);
  }
  /* Front */
  .card-front { top: 40px; background: var(--brand-red); }
  .front-name {
    position: absolute; left: 0; right: 0; top: 150px;
    text-align: center; color: var(--card-white);
    font-weight: 900; font-size: 84px; letter-spacing: 1px;
  }
  .front-web {
    position: absolute; left: 34px; bottom: 30px;
    color: var(--card-white); font-size: 17px; letter-spacing: 2px;
  }
  .social-dots {
    position: absolute; right: 28px; top: 28px; display: flex; gap: 6px;
  }
  .social-dots span {
    width: 15px; height: 15px; border-radius: 50%; background: var(--card-white);
  }
  /* Back */
  .card-back { top: 500px; background: var(--card-white); }
  .back-swoosh { position: absolute; inset: 0; }
  .wordmark {
    position: absolute; left: 250px; top: 28px;
    color: var(--brand-red); font-weight: 900; font-size: 56px;
  }
  .holder { position: absolute; left: 262px; top: 102px; }
  .holder-name { color: var(--brand-red); font-weight: 700; font-size: 22px; }
  .holder-title { color: var(--text-grey); font-size: 17px; margin-top: 2px; }
  .contact-list {
    position: absolute; left: 28px; top: 190px; list-style: none;
    color: var(--card-white); font-size: 16px;
  }
  .contact-list li { display: flex; align-items: center; gap: 9px; height: 24px; }
  .contact-list svg { width: 15px; height: 15px; fill: var(--card-white); }
  .address {
    position: absolute; right: 40px; bottom: 24px;
    color: var(--card-white); font-size: 16px; line-height: 23px; text-align: right;
  }
</style>
</head>
<body>

<section class="card card-front">
  <div class="social-dots" aria-label="Social links"><span></span><span></span><span></span><span></span></div>
  <div class="front-name">Corvane</div>
  <div class="front-web">www.corvane-shelving.co.uk</div>
</section>

<section class="card card-back">
  <svg class="back-swoosh" viewBox="0 0 720 410" preserveAspectRatio="none">
    <path d="M0 88 C 160 128, 380 218, 720 243 L 720 253 C 380 228, 160 138, 0 98 Z" fill="var(--swoosh-grey)"/>
    <path d="M0 110 C 160 150, 380 240, 720 265 L 720 410 L 0 410 Z" fill="var(--brand-red)"/>
  </svg>

  <div class="wordmark">Corvane</div>
  <div class="holder">
    <div class="holder-name">Daniel ashworth</div>
    <div class="holder-title">Technical sales</div>
  </div>

  <ul class="contact-list">
    <li><svg viewBox="0 0 16 16"><path d="M3 1h3l1.5 4-2 1.5a9 9 0 0 0 4 4L11 8.5l4 1.5v3a2 2 0 0 1-2 2A13 13 0 0 1 1 3a2 2 0 0 1 2-2z"/></svg>01632 960481</li>
    <li><svg viewBox="0 0 16 16"><path d="M4 0h8a1 1 0 0 1 1 1v14a1 1 0 0 1-1 1H4a1 1 0 0 1-1-1V1a1 1 0 0 1 1-1zm1 2v10h6V2z"/></svg>07700 900317</li>
    <li><svg viewBox="0 0 16 16"><path d="M4 1h7l2 2v4H4zM1 7h14v6h-2v2H3v-2H1zm4 4v3h6v-3z"/></svg>01632 960592</li>
    <li><svg viewBox="0 0 16 16"><path d="M1 3h14v10H1zm1.5 1.3V5l5.5 4 5.5-4v-.7z"/></svg>daniel@corvane-shelving.co.uk</li>
  </ul>

  <div class="address">
    Twenty mill close<br>
    hartwell gate business Park<br>
    alderton, Derbyshire DE9 4QT<br>
    www.corvane-shelving.co.uk
  </div>
</section>

</body>
</html>
```